Halvard Quarry Company needs a company newsletter template

We need a 2-page editable newsletter template, that we can update monthly with various information and pictures. We would like an area to include our values: Be Safe, Be Honest, Be Responsible, Be Respectful, Be Great. Ideally we would have 2-3 bulk text areas to highlight different things each month, with area we an update a picture from time to time and maybe some text areas where we can add a fun fact type thing. Some of the areas we will include are production milestones (if any), monthly tenure, monthly new hires, highlighting an employee that demonstrates our value, community engagement, upcoming holidays/events, press releases. The exact content will likely change month to month but these will be some of the frequent topics. We are a copper Mine in northern Yukon. I've attached our Brand Guidelines and logo files. Our website is brelcoreworks.com if you want to see the style and type of photos from our site

```html
<!DOCTYPE html>
<html lang="en">
<head>
<meta charset="utf-8">
<title>Halvard Quarry Company – Newsletter Template</title>
<link href="https://fonts.googleapis.com/css2?family=Montserrat:ital,wght@0,300;0,400;0,600;0,700;0,900;1,400&family=Tinos:ital@1&display=swap" rel="stylesheet">
<style>
  :root{
    --rust:#7c2d1d;
    --rust-dark:#64231a;
    --rust-text:#8a2f1f;
    --gold:#f0be28;
    --navy:#243244;
    --ink:#3a3a3a;
    --paper:#ffffff;
    --canvas:#eeede9;
  }
  *{box-sizing:border-box;margin:0;padding:0}
  html,body{width:1200px;height:961px;overflow:hidden}
  body{background:var(--canvas);position:relative;font-family:"Montserrat",sans-serif;color:var(--ink)}

  .page{position:absolute;top:118px;width:560px;height:725px;background:var(--paper);overflow:hidden;box-shadow:0 2px 8px rgba(0,0,0,.12)}
  .page--front{left:30px}
  .page--back{left:610px}

  /* Masthead */
  .masthead{position:relative;height:95px;background:linear-gradient(100deg,var(--rust-dark) 0%,var(--rust) 45%,#8a3622 70%,var(--rust) 100%)}
  .brand{position:absolute;left:0;top:0;width:156px;height:95px;display:flex;align-items:center;justify-content:center;gap:6px;padding:0 10px}
  .brand__mark{width:9px;height:9px;background:var(--gold);flex:none}
  .brand__name{font-weight:700;font-size:11px;line-height:1.25;color:#fff;letter-spacing:.02em;text-transform:uppercase}
  .masthead__title{position:absolute;left:167px;top:10px;font-weight:300;font-size:55px;letter-spacing:.02em;color:var(--gold);line-height:1}
  .values{position:absolute;left:156px;right:0;bottom:0;height:19px;background:var(--gold);color:var(--rust-dark);font-size:9.6px;line-height:19px;padding-left:15px;letter-spacing:.01em}

  /* Front page */
  .sidebar{position:absolute;left:0;top:95px;width:156px;bottom:0;background:var(--navy);padding:24px 12px 0 26px}
  .section-head{position:relative;font-weight:900;font-size:16.5px;line-height:18.5px;color:#fff}
  .section-head span{display:block;color:var(--gold)}
  .section-head::before{content:"";position:absolute;left:-26px;top:3px;width:13px;height:13px;background:linear-gradient(135deg,var(--gold) 50%,#c5401f 50%)}
  .hire-photo{width:117px;height:76px;margin:11px 0 22px;background:linear-gradient(160deg,#c89a6a 0%,#8a7060 45%,#3f3a36 100%)}
  .note{font-family:"Tinos",serif;font-style:italic;font-size:7px;line-height:9px;color:#fff;margin-bottom:9px}
  .sidebar .section-head.second{margin-top:16px}
  .sidebar .section-head.second + .note{margin-top:7px}

  .main{position:absolute;left:156px;top:95px;right:0;bottom:0}
  .hero{position:relative;height:262px;background:linear-gradient(180deg,#5f8fc4 0%,#a9c7e6 35%,#dfe6ea 55%,#9c9486 68%,#6b5a48 100%)}
  .hero__headline{position:absolute;left:23px;top:18px;font-size:27.5px;line-height:27px;color:#3b3b3b;font-weight:300}
  .hero__headline b{font-weight:900;color:var(--rust-text)}
  .body-copy{padding:22px 25px 0 24px;font-size:9.3px;line-height:12.6px;color:#333}
  .body-copy p{margin-bottom:12.6px}
  .dropcap::first-letter{float:left;font-weight:300;font-size:40px;line-height:34px;color:var(--rust-text);margin:1px 4px 0 0}

  /* Back page */
  .article{height:309px;padding:15px 26px 0 26px;display:grid;grid-template-columns:1fr 1fr;column-gap:30px;font-size:9.3px;line-height:12.6px;color:#333;overflow:hidden}
  .article p{margin-bottom:12.6px}
  .features{height:321px;background:var(--navy);display:grid;grid-template-columns:1fr 1fr 1fr;padding:10px 10px 0 25px;column-gap:25px}
  .feature{position:relative;padding-right:6px}
  .feature + .feature::before{content:"";position:absolute;left:-13px;top:5px;bottom:22px;width:1px;background:#8a3a28}
  .feature .note{margin:0 0 9px}
  .feature .section-head{margin-bottom:9px}
</style>
</head>
<body>

<!-- Page one -->
<section class="page page--front">
  <header class="masthead">
    <div class="brand"><span class="brand__mark"></span><span class="brand__name">Halvard Quarry Company</span></div>
    <h1 class="masthead__title">NEWSLETTER</h1>
    <div class="values">BE SAFE, BE HONEST, BE RESPONSIBLE, BE RESPECTFUL, BE GREAT.</div>
  </header>

  <aside class="sidebar">
    <h2 class="section-head">Monthly<span>New Hires</span></h2>
    <div class="hire-photo" role="img" aria-label="Photo of a new hire in a hard hat and safety vest holding a clipboard"></div>
    <p class="note">Lorem ipsum dolor sit amet, consectetur adipiscing elit. Duis risus libero, condim enin. Curabitur non condimentum diam. Morbi suscipit, risus non maximus semper, elit nisl placerat augue.</p>
    <p class="note">Nulla id vehicula tellus. Duis vitae cons equat dolor. Fusce ultricies tortor ipsum, aam est.</p>
    <p class="note">Nunc pretium libero hendrerit justo cons ectetur ornare. Etiam dictum metus id tu rpis volutpat, nec interdum ipsum phaas retra. tibulum molestie dignissim.</p>

    <h2 class="section-head second">Press<span>Releases</span></h2>
    <p class="note">Lorem ipsum dolor sit amet, consectetur adipiscing elit. Duis risus libero, condim enin. Curabitur non condimentum diam. Morbi suscipit, risus non maximus semper, elit nisl placerat augue.</p>
    <p class="note">Nulla id vehicula tellus. Duis vitae cons equat dolor. Fusce ultricies tortor ipsum. Nulla id vehicula tellus. Duis vitae cons equat dolor. Fusce ultricies tortor ipsum. Nulla id vehicula tellus. Duis vitae cons equat dolor. Fusce ultricies tortor ipsum.</p>
    <p class="note">Nunc pretium libero hendrerit justo cons ectetur ornare. Etiam dictum metus id tu rpis volutpat, nec interdum us id tu rpis volutpat, nec interdum ipsum phaas retra. tibulum molestie dignissim.</p>
  </aside>

  <main class="main">
    <div class="hero" role="img" aria-label="Photo of a large yellow haul truck at an open-pit mine under a blue sky">
      <h2 class="hero__headline"><b>TITTLE HERE</b> AMET<br>LOREMIPSUM<br><b>DOLORSIT</b></h2>
    </div>
    <div class="body-copy">
      <p class="dropcap">Lorem ipsum dolor sit amet, consectetur adipiscing elit. Duis risus libero, condimentum in molestie quis, gravida non justo. Integer aliquam tellus id nisl fringilla sollicitudin. Curabitur non condimentum diam. Morbi suscipit, risus non maximus semper, elit nisl placerat augue, id pharetra nulla neque ac diam. Curabitur eu malesuada nunc. Phasellus in aliquam lectus, et blandit enim. Mauris dignissim varius tortor, et tincidunt augue euismod sit amet. In hac habitasse platea dictumst. Praesent enim est, rutrum et velit quis, lobortis cursus dui. Praesent ultrices, mi in molestie efficitur, est urna scelerisque nunc, quis vestibulum eros risus vitae lectus.</p>
      <p>Nulla id vehicula tellus. Duis vitae consequat dolor. Fusce ultricies tortor ipsum, ac tempus mi iaculis et. Fusce quis fermentum enim. Curabitur tempus suscipit faucibus. Sed eu cursus orci, tincidunt tincidunt turpis. Vestibulum ante ipsum primis in faucibus orci luctus et ultrices posuere cubilia curae; Donec turpis turpis, pretium non elit quis, fermentum dignissim massa. Nam vitae odio non augue mattis malesuada. Etiam est diam, ullamcorper lacinia rhoncus quis, gravida venenatis magna.</p>
      <p>Nunc pretium libero hendrerit justo consectetur ornare. Etiam dictum metus id turpis volutpat, nec interdum ipsum pharetra. Sed et vestibulum dolor. Nam sapien nibh, dictum nec lacinia non, laoreet in nulla. Vestibulum molestie dignissim tristmpus suscipit faucibus. Sed eu cursus orci, tincidunt tincidunt turpis. Vestibulum ante ipsum primis in faucibus orci luctus et ultrices posuere cubilia curae; Donec tumpus suscipit faucibus. Sed eu cursus orci, tincidunt tincidunt turpis. Vestibulum ante ipsum primis in faucibus orci luctus et ultrices posuere cubilia curae; Donec tuique. Nulla pellentesque.</p>
    </div>
  </main>
</section>

<!-- Page two -->
<section class="page page--back">
  <header class="masthead">
    <div class="brand"><span class="brand__mark"></span><span class="brand__name">Halvard Quarry Company</span></div>
    <h1 class="masthead__title">NEWSLETTER</h1>
    <div class="values">BE SAFE, BE HONEST, BE RESPONSIBLE, BE RESPECTFUL, BE GREAT.</div>
  </header>

  <article class="article">
    <div>
      <p class="dropcap">Lorem ipsum dolor sit amet, consectetur adipiscing elit. Duis risus libero, condi ment um in molestie quis, gravida non justo. Integer aliquam tellus id nisl fringilla sollicitudin. Curabitur non condimentum diam. Morbi suscipit, risus non maximus semper, elit nisl placerat augue, id pharetra nulla neque ac diam. Curabitur eu malesuada nunc. Phasellus in aliquam lectus, et blandit enim. Mauris dignissim varius tortor, et tincidunt augue euismod sit amet. In hac habitasse platea dictumst. Praesent enim est, rutrum et velit quis, lobortis cursus dui.</p>
      <p>Nulla id vehicula tellus. Duis vitae consequat dolor. Fusce ultricies tortor ipsum, ac tempus mi iaculis et. Fusce quis fermentum enim. Curabitur tempus suscipit faucibus. Sed eu cursus orci, tincidunt tincidunt turpis. Vest fermentum enim. Curabitur tempus suscipit faucibus. Sed eu cursus orci, tincidunt tincidunt turpis. Vestibuluibulum ante ipsum primis in faucibus orci luctus et ultrices posuere cubilia curae; Donec turpis turpis, pretium</p>
    </div>
    <div>
      <p>non elit quis, fermentum dignissim massa. Nam vitae odio non augue mattis malesuada. Etiam est diam, ullamc orper lacinia rhoncus quis, gravida venenatis magna. Nunc pretium libero hendrerit justo consectetur ornare. Etiam dictum metus id turpis volutpat, nec interdum ipsum pharetra. Sed et vestibulum dolor. Nam sapien nibh, dictum nec lacinia non, laoreet in nulla. Vestibulum molestie dignissim tristique. Nulla pellentesque urna leo, nec malesuada diam elementum elementum. Proin eget ipsum ligula.</p>
      <p>Donec fringilla, turpis sed convallis vestibulum, nunc augue hendrerit enim, ac fermentum arcu lorem at lectus. Sed ultricies lobortis neque, a porta est pre ium id. Sed magna s massa. Sed in mauris ac ante cursus pul vinar. Aenean molestie congueem, laoreet vitae viverra ut, lacinia in massa. Sed in mauris ac ante cursus pul vinar. Aenean molestie congue erat, nec porttitor urna vel ue et. Nam auctor purus lorem, vitae pharetra mi dapibus non. Ut mollis neque vita.</p>
    </div>
  </article>

  <section class="features">
    <div class="feature">
      <h2 class="section-head">Production<span>Milestones</span></h2>
      <p class="note">Lorem ipsum dolor sit amet, consectetur adipiscing elit. Duis risus libero, condim enin. Curabitur non condimentum diam. Morbi suscipit, risus non maximus semper, elit nisl placerat augue.</p>
      <p class="note">Nulla id vehicula tellus. Duis vitae cons equat dolor. Fusce ultricies tortor ipsum, aam est diat dolor. Fusce ul tri cies tortor ipsum, aam est diam, ul lam corper lacinia rhon cus quis, gravida venenatis</p>
      <p class="note">Nunc pretium libero hendrerit justo cons ectetur dignissim tristique. Nulla pellentesque urna leo, nec malesuada diam elementum elementum. Proin eget ipsum nec interdum ipsum phaas retra. tibulum molestie dignissim tristique. Nulla pellentesque urna leo, nec malesuada diam elementum. Proin eget ipsum nec interdum ipsum phaas retra. tibulum molestie dign issim tristique. Nulla pellentesque urna</p>
    </div>
    <div class="feature">
      <h2 class="section-head">Community<span>Engagement</span></h2>
      <p class="note">Lorem ipsum dolor sit amet, consectetur adipiscing elit. Duis risus libero, condim enin. Curabitur non condimentum diam. Morbi suscipit, risus non maximus semper, elit nisl placerat augue.</p>
      <p class="note">Nulla id vehicula tellus. Duis vitae cons equat dolor. Fusce ultricies tortor ipsum, aam est diat dolor. Fusce ul tri cies tortor ipsum, aam est diam, ul lam corper lacinia rhon cus quis, gravida venenatis</p>
      <p class="note">Nunc pretium libero hendrerit justo cons ectetur dignissim tristique. Nulla pellentesque urna leo, nec malesuada diam elementum elementum. Proin eget ipsum nec interdum ipsum phaas retra. tibulum molestie dignissim tristique. Nulla pellentesque urna leo, nec malesuada diam elementum. Proin eget ipsum nec interdum ipsum phaas retra. tibulum molestie dign issim tristique. Nulla pellentesque urna</p>
    </div>
    <div class="feature">
      <h2 class="section-head">Upcoming<span>Holidays/events</span></h2>
      <p class="note">Lorem ipsum dolor sit amet, consectetur adipiscing elit. Duis risus libero, condim enin. Curabitur non condimentum diam. Morbi suscipit, risus non maximus semper, elit nisl placerat augue.</p>
      <p class="note">Nulla id vehicula tellus. Duis vitae cons equat dolor. Fusce ultricies tortor ipsum, aam est diat dolor. Fusce ul tri cies tortor ipsum, aam est diam, ul lam corper lacinia rhon cus quis, gravida venenatis</p>
      <p class="note">Nunc pretium libero hendrerit justo cons ectetur dignissim tristique. Nulla pellentesque urna leo, nec malesuada diam elementum elementum. Proin eget ipsum nec interdum ipsum phaas retra. tibulum molestie dignissim tristique. Nulla pellentesque urna leo, nec malesuada diam elementum. Proin eget ipsum nec interdum ipsum phaas retra. tibulum molestie dign issim tristique. Nulla pellentesque urna</p>
    </div>
  </section>
</section>

</body>
</html>
```